Billboard for Local Roofing Company

The billboard we are using will be 12' tall and 24' wide. We are looking for a clean design that is not too busy, one that stands out and is easily readable. The branding colors used should match the colors in our logo. On the billboard, it should have our slogan "Where Every Shingle Thing Matters" with the word "Shingle" in the orange.
It should also have the KNR Crestline Pro logo uploaded here as well.
Lastly, it should have our phone number 928-555-0147 and our website www.corvane-roofing.com.
I have uploaded a stock image we are thinking about using in the background of the sign...this could be darkened or otherwise obscured.
- Match fonts up if possible

```html
<!DOCTYPE html>
<html lang="en">
<head>
<meta charset="utf-8">
<title>Corvane Roofing Billboard</title>
<link rel="stylesheet" href="https://fonts.googleapis.com/css2?family=Oswald:wght@500;600&family=Arvo:wght@700&display=swap">
<style>
  :root {
    --page-bg: #d2d2d2;
    --board-black: #0a0a0a;
    --brand-orange: #e4571d;
    --text-white: #ffffff;
    --roof-dark: #2c2d33;
    --roof-mid: #4a4b52;
    --badge-tone: #55565e;
  }
  * { margin: 0; padding: 0; box-sizing: border-box; }
  html, body {
    width: 882px;
    height: 1200px;
    overflow: hidden;
    background: var(--page-bg);
  }
  .billboard {
    position: absolute;
    left: 60px;
    top: 410px;
    width: 762px;
    height: 380px;
    background: var(--board-black);
    overflow: hidden;
    box-shadow: 0 4px 10px rgba(0,0,0,0.35);
  }
  .roof-photo {
    position: absolute;
    inset: 0;
    background:
      linear-gradient(90deg, var(--board-black) 0%, var(--board-black) 30%, rgba(10,10,10,0.55) 55%, rgba(10,10,10,0.1) 100%),
      linear-gradient(150deg, var(--roof-mid) 0%, var(--roof-dark) 45%, var(--roof-mid) 70%, var(--roof-dark) 100%);
  }
  .frame {
    position: absolute;
    inset: 0;
    width: 762px;
    height: 380px;
  }
  .brand-name {
    position: absolute;
    left: 49px;
    top: 112px;
    font-family: "Arvo", serif;
    font-weight: 700;
    font-size: 37px;
    color: var(--text-white);
    line-height: 1;
  }
  .slogan {
    position: absolute;
    left: 45px;
    top: 160px;
    font-family: "Oswald", sans-serif;
    font-weight: 600;
    font-size: 50px;
    line-height: 50px;
    color: var(--text-white);
    text-transform: uppercase;
    letter-spacing: -0.5px;
  }
  .slogan .accent { color: var(--brand-orange); }
  .phone {
    position: absolute;
    left: 44px;
    top: 266px;
    font-family: "Oswald", sans-serif;
    font-weight: 600;
    font-size: 64px;
    line-height: 1;
    color: var(--brand-orange);
    letter-spacing: -0.5px;
  }
  .website {
    position: absolute;
    left: 208px;
    top: 342px;
    width: 346px;
    text-align: center;
    font-family: "Oswald", sans-serif;
    font-weight: 500;
    font-size: 24px;
    line-height: 28px;
    letter-spacing: 1.2px;
    color: var(--text-white);
  }
  .certification-badge {
    position: absolute;
    left: 627px;
    top: 256px;
    width: 76px;
    height: 76px;
    border-radius: 50%;
    background: var(--badge-tone);
  }
</style>
</head>
<body>
  <div class="billboard">
    <div class="roof-photo" role="img" aria-label="Darkened photo of a grey asphalt shingle roof"></div>

    <svg class="frame" viewBox="0 0 762 380" aria-hidden="true">
      <polyline points="207,358 22,358 22,21 739,21 739,358 555,358"
                fill="none" stroke="var(--brand-orange)" stroke-width="2"/>
    </svg>

    <div class="brand-name">Corvane Roofing</div>

    <h1 class="slogan">Where Every <span class="accent">Shingle</span><br>Thing Matters</h1>

    <div class="phone">928-555-0147</div>

    <div class="certification-badge" role="img" aria-label="KNR Crestline Pro certification badge"></div>

    <div class="website">www.corvane-roofing.com</div>
  </div>
</body>
</html>
```